brightlakePRESS is publishing a new book and needs some exceptional cover and layout design!

We are publishing a narrow niche PDF eBook and need both a great cover AND great magazine style layout.

The eBook is a compilation of interviews with 12 financial experts on a particular topic. So the format is is the same for each interview 'chapter'

We are looking for a good front cover/document design that will make what is a pretty dry topic, exciting, interesting and easy to read. Basically - magazine style layout.

The specs for the front cover are:

Title:

The Hurdles and Openings Before Bookkeepers and Planners In Expanding Their Pension Fund Practice In 2014 -2015

by Tom Vellani

published by brightlakePRESS

The client would like a similar cover to the one I have attached for your reference. (book front cover example). By no means be limited by this design suggestion. The only caveat is that shots of all interview subjects are included (except the author). These have been included in the zip file.

The design for the text should be elegant and consistent with the design of the front cover. Please format the text in pages 1 to 15 to demonstrate you've understood the brief.

Attached files.

1) MS word version of draft book pages 1 to 15
2) copy of the cover my client would like to emulate.

reminder - this is destined to be a PDF eBook - so looking for some nice eye catching magazine style layout in the design. Columns would be fine.

Good luck!

Brent Marlow
brightlakePRESS

Target Market(s)

Professional Accountants who are running there own businesses

Industry/Entity Type

Financial

Colors

Designer to choose colors to be used in the design.

Requirements
Must have
• The cover must feature headshots of all the interview subjects. The PDF layout must be optimised for viewing on an iPad

```html
<!DOCTYPE html>
<html lang="en">
<head>
<meta charset="utf-8">
<title>The Hurdles and Openings – Cover and Dedication Page</title>
<link rel="stylesheet" href="https://fonts.googleapis.com/css2?family=PT+Sans+Narrow:wght@400;700&family=Yellowtail&display=swap">
<style>
  :root {
    --backdrop: #1b1b1c;
    --page-dark: #2a1c1d;
    --band-dark: #2a1e1f;
    --ink-light: #f4eeee;
    --ink-muted: #e2d8d8;
    --title-blue: #2c50a2;
    --ink-dark: #2a2a2a;
    --sky-top: #ffffff;
    --sky-blue: #c9dcee;
    --chart-green: #58b847;
  }
  * { box-sizing: border-box; margin: 0; padding: 0; }
  html, body { width: 1200px; height: 1017px; overflow: hidden; }
  body {
    position: relative;
    background: var(--backdrop);
    font-family: "PT Sans Narrow", "Arial Narrow", sans-serif;
  }

  /* Dedication page */
  .dedication-page {
    position: absolute; left: 44px; top: 42px;
    width: 541px; height: 702px;
    background: var(--page-dark);
    color: var(--ink-light);
  }
  .pen-photo {
    position: absolute; left: 440px; top: 150px;
    width: 101px; height: 180px;
    background: radial-gradient(ellipse at 75% 40%, #3a2a2a 0%, rgba(42,28,29,0) 70%);
  }
  .dedication-text {
    position: absolute; left: 0; width: 100%; top: 140px;
    text-align: center; font-size: 15px; line-height: 21px;
  }
  .thanks-script {
    position: absolute; left: 196px; top: 222px;
    font-family: "Yellowtail", cursive; font-size: 34px;
    color: var(--ink-light);
    transform: rotate(-8deg);
    line-height: 30px;
  }
  .thanks-script span { display: block; padding-left: 106px; }
  .acknowledgement {
    position: absolute; left: 0; width: 100%; top: 313px;
    text-align: center; font-size: 15px; line-height: 21px;
  }
  .imprint {
    position: absolute; left: 37px; top: 474px; width: 480px;
    font-size: 7.6px; line-height: 11.6px; color: var(--ink-muted);
  }
  .imprint p { margin-bottom: 11.6px; }

  /* Front cover */
  .front-cover {
    position: absolute; left: 619px; top: 275px;
    width: 542px; height: 701px;
    background: #fff; overflow: hidden;
  }
  .cover-hero {
    position: absolute; left: 0; top: 0; width: 100%; height: 428px;
    background: linear-gradient(200deg, var(--sky-blue) 0%, #e6eff8 45%, var(--sky-top) 75%);
  }
  .hero-graphic {
    position: absolute; left: 340px; top: 150px; width: 202px; height: 278px;
    background:
      radial-gradient(ellipse 60% 45% at 62% 40%, rgba(88,184,71,0.9) 0%, rgba(88,184,71,0.5) 55%, rgba(88,184,71,0) 100%),
      radial-gradient(ellipse 70% 30% at 50% 82%, rgba(201,154,124,0.85) 0%, rgba(201,154,124,0) 100%),
      radial-gradient(ellipse 50% 25% at 25% 100%, rgba(74,68,70,0.8) 0%, rgba(74,68,70,0) 100%);
  }
  .cover-title {
    position: absolute; left: 35px; top: 48px;
    color: var(--title-blue); font-weight: 700;
    font-size: 62px; line-height: 76px; letter-spacing: 0.5px;
  }
  .cover-subtitle {
    position: absolute; left: 35px; top: 200px;
    color: var(--ink-dark); font-size: 31px; line-height: 48px;
  }
  .expert-band {
    position: absolute; left: 0; top: 428px; width: 100%; height: 169px;
    background: var(--band-dark);
  }
  .headshot-grid {
    position: absolute; left: 35px; top: 17px;
    display: grid; grid-template-columns: repeat(8, 55.5px); grid-auto-rows: 67px;
  }
  .headshot { background: linear-gradient(180deg, #b9b1aa 0%, #7b716c 100%); }
  .headshot:nth-child(even) { background: linear-gradient(180deg, #d4cfc9 0%, #5e5a58 100%); }
  .headshot:nth-child(3n) { background: linear-gradient(180deg, #c7b9a6 0%, #6e6763 100%); }
  .headshot:nth-child(5n) { background: linear-gradient(180deg, #9fb09a 0%, #4f524d 100%); }
  .headshot:nth-child(4n+1) { background: linear-gradient(180deg, #a9b6c2 0%, #5d6166 100%); }
  .cover-credits {
    position: absolute; left: 35px; top: 620px; color: var(--ink-dark);
  }
  .author { font-weight: 700; font-size: 19px; line-height: 22px; }
  .publisher { font-size: 16px; line-height: 22px; }
</style>
</head>
<body>

<section class="dedication-page">
  <div class="pen-photo" role="img" aria-label="Photo of a hand writing with a fountain pen"></div>
  <p class="dedication-text">
    I dedicate this book to my loving and supportive wife Elaine.<br>
    We have been working together now for more then 20 years and<br>
    most people that know her say she is the better half and I agree.
  </p>
  <p class="thanks-script">Thank you<span>Darling</span></p>
  <p class="acknowledgement">
    I would also like to thank my good friend and business partner Brent<br>
    Marlow who made this eBook possible.
  </p>
  <div class="imprint">
    <p>Copyright © 2014 by Tom Vellani</p>
    <p>All rights reserved. No part of this publication may be reproduced, distributed or transmitted in any form or by any means, including photocopying, recording, or other electronic or mechanical methods, without the prior written permission of the publisher, except in the case of brief quotations embodied in critical reviews and certain other noncommercial uses permitted by copyright law. For permission requests, write to the publisher, addressed “Attention: Permissions Coordinator,” at the address below.</p>
    <p>Tom Vellani/published by brightlakePRESS<br>Street Address<br>14/2 Harlow St<br>Bayview Heights NSW<br>2601<br>www.brightlakepress.com.au</p>
    <p>The Hurdles and Openings Before Bookkeepers and Planners In Expanding Their Pension Fund Practice<br>In 2014 -2015/ Tom Vellani. —1st ed.<br>ISBN 978-0-0000000-4-2</p>
  </div>
</section>

<section class="front-cover">
  <div class="cover-hero"></div>
  <div class="hero-graphic" role="img" aria-label="Illustration of an open hand holding a rising green bar chart with an upward arrow"></div>
  <h1 class="cover-title">THE HURDLES &amp;<br>OPENINGS</h1>
  <p class="cover-subtitle">Before Bookkeepers and<br>Planners In Expanding<br>Their Pension Fund Practice<br>In 2014 -2015</p>
  <div class="expert-band">
    <div class="headshot-grid">
      <div class="headshot" role="img" aria-label="Headshot of interview subject 1"></div>
      <div class="headshot" role="img" aria-label="Headshot of interview subject 2"></div>
      <div class="headshot" role="img" aria-label="Headshot of interview subject 3"></div>
      <div class="headshot" role="img" aria-label="Headshot of interview subject 4"></div>
      <div class="headshot" role="img" aria-label="Headshot of interview subject 5"></div>
      <div class="headshot" role="img" aria-label="Headshot of interview subject 6"></div>
      <div class="headshot" role="img" aria-label="Headshot of interview subject 7"></div>
      <div class="headshot" role="img" aria-label="Headshot of interview subject 8"></div>
      <div class="headshot" role="img" aria-label="Headshot of interview subject 9"></div>
      <div class="headshot" role="img" aria-label="Headshot of interview subject 10"></div>
      <div class="headshot" role="img" aria-label="Headshot of interview subject 11"></div>
      <div class="headshot" role="img" aria-label="Headshot of interview subject 12"></div>
      <div class="headshot" role="img" aria-label="Headshot of interview subject 13"></div>
      <div class="headshot" role="img" aria-label="Headshot of interview subject 14"></div>
      <div class="headshot" role="img" aria-label="Headshot of interview subject 15"></div>
    </div>
  </div>
  <div class="cover-credits">
    <p class="author">by Tom Vellani</p>
    <p class="publisher">published by brightlakePRESS</p>
  </div>
</section>

</body>
</html>
```